Teskar Business Cards

We need new Business Cards for our startup. It just launched.It is working in the high-end it-market. Specifically in the cloud area. We are a hybrid cloud company. The company logo is attached. We are a Swiss based company. Information visible on the card is: 1. Logo 2. Company Name: Teskar AG 3. Subtitle: Hybrid Clouds. 3. Name: Lukas Brenner 4. Adress: Holderweg 12a, 8462 Seewil, Switzerland 5. Email: lukas@teskar.example. 6. Mobile: +41 79 304 62 18. It should be a grey/white design. Similar to the attached logo. It should have class, high-quality but not too much color and no gold used.

I forgot to add my Position. Please use Founder / CEO. thanks lukas

```html
<!DOCTYPE html>
<html lang="en">
<head>
<meta charset="utf-8">
<title>Teskar AG – Business Card</title>
<link rel="stylesheet" href="https://fonts.googleapis.com/css2?family=Bitter:wght@400;500&family=Barlow:wght@300;400&display=swap">
<style>
  :root {
    --page-bg: #e4e2de;
    --card-bg: #f7f6f3;
    --ink: #2b2b2b;
    --ink-soft: #4a4a4a;
    --label-grey: #9a9a9a;
    --accent-grey: #a3a3a3;
    --mark-grey: #d6d5d1;
    --card-shadow: rgba(0, 0, 0, 0.12);
  }
  * { margin: 0; padding: 0; box-sizing: border-box; }
  html, body {
    width: 1200px;
    height: 900px;
    overflow: hidden;
    background: var(--page-bg);
  }
  .canvas {
    position: relative;
    width: 1200px;
    height: 900px;
  }
  .business-card {
    position: absolute;
    left: 100px;
    top: 126px;
    width: 1000px;
    height: 648px;
    background: var(--card-bg);
    box-shadow: 0 6px 24px var(--card-shadow);
  }
  .brand {
    position: absolute;
    left: 400px;
    top: 108px;
    display: flex;
    align-items: center;
    gap: 34px;
  }
  .brand-dot {
    width: 26px;
    height: 26px;
    border-radius: 50%;
    background: var(--mark-grey);
  }
  .brand-name {
    font-family: "Barlow", sans-serif;
    font-weight: 300;
    font-size: 62px;
    letter-spacing: 0.42em;
    color: var(--ink-soft);
  }
  .person {
    position: absolute;
    left: 150px;
    top: 378px;
    text-align: right;
  }
  .person-name {
    font-family: "Bitter", serif;
    font-weight: 500;
    font-size: 34px;
    color: var(--ink);
  }
  .person-role {
    margin-top: 8px;
    font-family: "Barlow", sans-serif;
    font-weight: 400;
    font-size: 22px;
    letter-spacing: 0.08em;
    color: var(--label-grey);
  }
  .contact {
    position: absolute;
    left: 520px;
    top: 316px;
    display: grid;
    grid-template-columns: auto auto 1fr;
    column-gap: 14px;
    row-gap: 10px;
    align-items: baseline;
  }
  .contact-label {
    font-family: "Barlow", sans-serif;
    font-size: 19px;
    letter-spacing: 0.12em;
    color: var(--label-grey);
  }
  .contact-sep {
    font-family: "Bitter", serif;
    font-size: 22px;
    color: var(--ink);
  }
  .contact-value {
    font-family: "Bitter", serif;
    font-size: 26px;
    color: var(--ink);
  }
  .address {
    position: absolute;
    left: 540px;
    top: 430px;
    font-family: "Bitter", serif;
    font-style: normal;
    font-size: 25px;
    line-height: 1.32;
    color: var(--ink);
  }
  .address-tagline { color: var(--accent-grey); }
</style>
</head>
<body>
<main class="canvas">
  <section class="business-card" aria-label="Teskar AG business card">
    <div class="brand">
      <span class="brand-dot" aria-hidden="true"></span>
      <span class="brand-name">TESKAR</span>
    </div>

    <div class="person">
      <p class="person-name">Lukas Brenner</p>
      <p class="person-role">FOUNDER / CEO</p>
    </div>

    <div class="contact">
      <span class="contact-label">MOBILE</span>
      <span class="contact-sep">:</span>
      <span class="contact-value">+41 79 304 62 18</span>
      <span class="contact-label">E-MAIL</span>
      <span class="contact-sep">:</span>
      <span class="contact-value">lukas@teskar.example</span>
    </div>

    <address class="address">
      Teskar AG – <span class="address-tagline">Hybrid Clouds</span><br>
      Holderweg 12a<br>
      8462 Seewil, Switzerland
    </address>
  </section>
</main>
</body>
</html>
```